Cool interactive one page web design for AI business (phase-1 design)

We are a (start-up) artificial intelligence company call Varitoken (soon to be @ varitoken.co). I'd like a cool one page design ready for our launch. I have specific ideas in mind.

The idea of the one pager is just to be able to place my logo on and give quick contact details, etc.

Please see this page for reference: http://brightmarlow.com/

On that page you will notice when you move your mouse that there is an effect around the edges where the 'Neurons' follow/join-up your mouse. I would like to replicate this effect for my one pager. However my neurons should have this effect across the page, not just on the sides. The background of the page will be black and we should have white neurons.

Please find attached a design example of what the page will look like.

Target Market(s)

Artificial intelligence, machine learning, publishers, media

Industry/Entity Type

Media

Requirements
Must have
• The interactive design I mentioned

```html
<!DOCTYPE html>
<html lang="en">
<head>
<meta charset="utf-8">
<title>Varitoken – Artificial Intelligence for Publishers</title>
<link href="https://fonts.googleapis.com/css2?family=Lato:wght@400;700;900&display=swap" rel="stylesheet">
<style>
:root{
  --navy:#2c2a8e;
  --magenta:#c4087f;
  --accent:#e4d331;
  --ink:#222;
  --muted:#555;
  --pale:#f1f1f1;
  --dark:#0b0b0b;
  --footer:#1b1b1b;
  --white:#fff;
}
*{box-sizing:border-box;margin:0;padding:0}
html,body{width:1200px;height:3509px;overflow:hidden}
body{font-family:'Lato',sans-serif;color:var(--ink);background:var(--white);position:relative}
section,header,footer{position:absolute;left:0;width:1200px}
.section-title{position:absolute;left:0;width:100%;text-align:center;color:var(--navy);font-weight:900;font-size:34px;letter-spacing:.5px}
.btn{position:absolute;display:flex;align-items:center;justify-content:center;background:var(--magenta);color:var(--white);font-weight:900;font-size:14px;letter-spacing:.5px;width:180px;height:48px;text-decoration:none}
.body-text{font-size:15px;line-height:29px;color:var(--ink)}

/* Hero */
.hero{top:0;height:742px;background:radial-gradient(ellipse at 50% 70%,#1d1d22 0%,var(--dark) 70%)}
.nav{position:absolute;top:0;left:75px;width:1050px;height:92px;border-bottom:1px solid #333;display:flex;justify-content:center}
.nav a{color:var(--white);font-size:14px;font-weight:700;text-decoration:none;padding:40px 21px 0;position:relative}
.nav a.active{color:var(--accent)}
.nav a.active::after{content:"";position:absolute;left:0;right:0;bottom:-1px;height:6px;background:var(--accent)}
.brand{position:absolute;top:150px;left:0;width:100%;display:flex;justify-content:center;align-items:center;gap:12px;color:var(--white);font-size:52px;font-weight:700}
.brand-dot{width:50px;height:50px;border-radius:50%;background:var(--magenta)}
.hero-kicker{position:absolute;top:248px;width:100%;text-align:center;color:var(--white);font-weight:900;font-size:26px}
.hero-title{position:absolute;top:282px;width:100%;text-align:center;color:var(--white);font-weight:700;font-size:34px;letter-spacing:.5px}
.hero-visual{position:absolute;left:362px;top:345px;width:470px;height:360px;border-radius:50% 45% 40% 45%;background:radial-gradient(circle at 40% 45%,rgba(230,120,60,.55),rgba(120,60,180,.4) 45%,rgba(40,120,200,.2) 70%,transparent 80%)}
.play{position:absolute;left:572px;top:336px}

/* Who we are */
.who{top:742px;height:371px}
.who .section-title{top:50px}
.who p{position:absolute;top:108px;left:170px;width:860px;text-align:center}
.who .btn{left:510px;top:262px}

/* What we do */
.what{top:1113px;height:618px}
.what-band{position:absolute;top:0;left:0;width:100%;height:421px;background:linear-gradient(120deg,#1d1b6e 0%,#2b2996 55%,#1a1860 100%)}
.what .section-title{top:48px;color:var(--white)}
.what .lead{position:absolute;top:108px;width:100%;text-align:center;color:var(--white);font-size:15px}
.cards{position:absolute;top:174px;left:77px;display:flex;gap:32px}
.card{position:relative;width:329px;height:381px;background:var(--white);box-shadow:0 0 0 1px #ddd,0 3px 8px rgba(0,0,0,.12);text-align:center}
.card svg{position:absolute;top:40px;left:132px}
.card h3{position:absolute;top:164px;width:100%;color:var(--navy);font-weight:900;font-size:19px}
.card p{position:absolute;top:192px;left:22px;width:285px;font-size:14px;line-height:25px}
.card .btn{left:74px;top:307px}

/* Clients */
.clients{top:1731px;height:215px;background:var(--pale)}
.clients .section-title{top:54px}
.client-row{position:absolute;top:118px;left:0;width:100%;display:flex;justify-content:center;gap:30px;align-items:center}
.client{display:flex;align-items:center;gap:6px;font-size:19px;font-weight:700;color:#333}
.client i{display:block;width:10px;height:10px;border-radius:50%;background:#999}

/* Blog */
.blog{top:1946px;height:468px;background:linear-gradient(90deg,#16233a 0%,#1d3050 50%,#0f1a2c 100%)}
.blog-visual{position:absolute;right:0;top:0;width:560px;height:468px;background:radial-gradient(ellipse at 55% 40%,rgba(60,200,230,.45),rgba(30,70,110,.3) 45%,transparent 75%)}
.blog h2{position:absolute;top:50px;left:75px;color:var(--white);font-weight:900;font-size:34px}
.blog h3{position:absolute;top:114px;left:75px;color:var(--magenta);font-weight:900;font-size:20px}
.blog p{position:absolute;top:144px;left:75px;width:580px;color:var(--white);font-size:15px;line-height:25px}
.blog .meta{position:absolute;top:262px;left:75px;color:var(--white);font-size:14px;font-weight:700;display:flex;gap:14px;align-items:center}
.blog .btn{left:75px;top:330px}
.dots{position:absolute;top:349px;left:576px;display:flex;gap:8px}
.dots span{width:9px;height:9px;border-radius:50%;background:#777}
.dots span:first-child{background:var(--white)}

/* Testimonials */
.say{top:2414px;height:440px}
.say .section-title{top:40px}
.quotes{position:absolute;top:112px;left:77px;display:flex;gap:32px}
.quote{position:relative;width:329px;height:290px;text-align:center}
.quote p{font-size:15px;line-height:27px}
.avatar{position:absolute;left:120px;top:122px;width:90px;height:90px;border-radius:50%;background:linear-gradient(#d8d8d8,#a9a9a9);border:3px solid #eee}
.quote-mark{position:absolute;left:198px;top:154px;width:34px;height:34px;border-radius:50%;background:var(--magenta);color:var(--white);font-weight:900;font-size:22px;line-height:38px}
.quote h4{position:absolute;top:226px;width:100%;color:var(--magenta);font-size:13px;font-weight:900}
.quote small{position:absolute;top:246px;left:0;width:100%;font-size:13px;color:#444}

/* News */
.news{top:2854px;height:428px;background:var(--pale)}
.news .section-title{top:38px}
.news-row{position:absolute;top:105px;left:77px;display:flex;gap:32px}
.news-item{width:329px}
.news-img{height:168px}
.news-item h4{margin-top:22px;color:var(--magenta);font-size:15px;font-weight:900}
.news-item p{font-size:14px;line-height:22px;margin-top:4px}

/* Footer */
.footer{top:3282px;height:227px;background:var(--footer);color:var(--white)}
.footer-brand{position:absolute;top:30px;left:75px;display:flex;align-items:center;gap:10px;font-size:34px;font-weight:700}
.footer-brand i{width:34px;height:34px;border-radius:50%;background:var(--magenta);display:block}
.copy{position:absolute;top:90px;left:75px;font-size:12px;line-height:20px;color:#aaa}
.social{position:absolute;top:148px;left:75px;display:flex;gap:14px;font-size:14px;font-weight:700;color:#ddd}
.footer h5{position:absolute;top:36px;font-size:14px;font-weight:900;letter-spacing:.5px}
.links{position:absolute;top:70px;display:grid;grid-template-columns:130px 100px;row-gap:12px;font-size:13px;color:#ddd}
.contact{position:absolute;top:70px;left:642px;font-size:13px;line-height:22px;color:#ddd}
.contact div{display:flex;gap:12px;align-items:center;margin-top:8px}
.signup-input{position:absolute;top:72px;left:883px;width:243px;height:38px;background:var(--white);color:#666;font-size:12px;padding:12px 10px}
.signup-btn{position:absolute;top:122px;left:1036px;width:90px;height:38px;background:var(--magenta);color:var(--white);font-size:12px;font-weight:900;display:flex;align-items:center;justify-content:center}
</style>
</head>
<body>

<header class="hero">
  <nav class="nav">
    <a class="active" href="#">HOME</a><a href="#">WHO WE ARE</a><a href="#">WHAT WE DO</a><a href="#">BLOG</a><a href="#">CLIENTS</a><a href="#">CAREERS</a><a href="#">NEWS</a><a href="#">CONTACT US</a>
  </nav>
  <div class="brand"><span class="brand-dot"></span>varitoken</div>
  <div class="hero-kicker">A NEW TYPE OF</div>
  <h1 class="hero-title">ARTIFICIAL INTELLIGENCE FOR PUBLISHER</h1>
  <div class="hero-visual" role="img" aria-label="Glowing circuit-board brain illustration"></div>
  <svg class="play" width="66" height="66" viewBox="0 0 66 66"><circle cx="33" cy="33" r="29" fill="none" stroke="#fff" stroke-width="5"/><path d="M26 20 L46 33 L26 46Z" fill="#fff"/></svg>
</header>

<section class="who">
  <h2 class="section-title">WHO WE ARE</h2>
  <p class="body-text">Aliquam molestie, mi et imperdiet euismod, dui purus auctor tellus, et interdum lacus lectus et ante. Sed accumsan sollicitudin sapien, sit amet adipiscing turpis gravida ac. In congue, neque ac lobortis volutpat, libero mauris varius mi, vitae suscipit ipsum ligula vitae risus. Duis aliquam nibh a dui iaculis viverra id a velit. Vivamus egestas risus in magna varius commodo. Etiam pretium porttitor lectus, vel ornare neque porta volutpat.</p>
  <a class="btn" href="#">READ MORE</a>
</section>

<section class="what">
  <div class="what-band" role="img" aria-label="Dark blue technology background"></div>
  <h2 class="section-title">WHAT WE DO</h2>
  <p class="lead">Aliquam molestie, mi et imperdiet euismod, dui purus auctor tellus, et interdum lacus lectus et ante.</p>
  <div class="cards">
    <article class="card">
      <svg width="64" height="64" viewBox="0 0 64 64" fill="none" stroke="#2c2a8e" stroke-width="4"><rect x="14" y="14" width="36" height="36" rx="4"/><path d="M22 6v8M32 6v8M42 6v8M22 50v8M32 50v8M42 50v8M6 22h8M6 32h8M6 42h8M50 22h8M50 32h8M50 42h8M24 26h16M24 32h16M24 38h16"/></svg>
      <h3>CONSECTETUER</h3>
      <p>Aliquam molestie, mi et imperdiet euismod, dui purus auctor tellus, et interdum lacus lectus et ante. Sed accumsan sollicitudin sapien, sit amet adipiscing...</p>
      <a class="btn" href="#">READ MORE</a>
    </article>
    <article class="card">
      <svg width="64" height="64" viewBox="0 0 64 64" fill="none" stroke="#2c2a8e" stroke-width="4"><path d="M32 6a18 18 0 0 0-10 33v7h20v-7A18 18 0 0 0 32 6z"/><path d="M24 52h16M27 58h10"/></svg>
      <h3>CONSECTETUER</h3>
      <p>Aliquam molestie, mi et imperdiet euismod, dui purus auctor tellus, et interdum lacus lectus et ante. Sed accumsan sollicitudin sapien, sit amet adipiscing...</p>
      <a class="btn" href="#">READ MORE</a>
    </article>
    <article class="card">
      <svg width="64" height="64" viewBox="0 0 64 64" fill="#2c2a8e"><circle cx="24" cy="36" r="16"/><circle cx="24" cy="36" r="6" fill="#fff"/><circle cx="46" cy="16" r="11"/><circle cx="46" cy="16" r="4" fill="#fff"/><circle cx="50" cy="48" r="8"/><circle cx="50" cy="48" r="3" fill="#fff"/></svg>
      <h3>CONSECTETUER</h3>
      <p>Aliquam molestie, mi et imperdiet euismod, dui purus auctor tellus, et interdum lacus lectus et ante. Sed accumsan sollicitudin sapien, sit amet adipiscing...</p>
      <a class="btn" href="#">READ MORE</a>
    </article>
  </div>
</section>

<section class="clients">
  <h2 class="section-title">CLIENTS</h2>
  <div class="client-row">
    <span class="client"><i></i>Brookvale</span><span class="client"><i></i>Quorvix</span><span class="client"><i></i>Netlane</span><span class="client"><i></i>Thymera</span><span class="client"><i></i>Kovana</span><span class="client"><i></i>Belvio</span><span class="client"><i></i>Mirantel</span><span class="client"><i></i>Adrena</span><span class="client"><i></i>Cirrano</span>
  </div>
</section>

<section class="blog">
  <div class="blog-visual" role="img" aria-label="Businessman holding a tablet with a glowing digital brain above it"></div>
  <h2>BLOG</h2>
  <h3>NAM FERMENTUM VESTIBULUM PURUS ID ALIQUET</h3>
  <p>Duis aliquam nibh a dui iaculis viverra id a velit. Vivamus egestas risus in magna varius commodo. Sed semper viverra egestas. Etiam pretium porttitor lectus, vel ornare neque porta volutpat. Aenean a nibh eget turpis vehicula tempus ac sed massa. Vestibulum dolor nulla, ultrices ac tincidunt sed, laoreet non est.</p>
  <div class="meta">
    <svg width="14" height="14" viewBox="0 0 14 14" fill="#fff"><rect x="1" y="3" width="12" height="10"/><rect x="3" y="1" width="2" height="3"/><rect x="9" y="1" width="2" height="3"/></svg>
    <span>Nov 03, 2017</span><span>|</span>
    <svg width="14" height="14" viewBox="0 0 14 14" fill="#fff"><circle cx="7" cy="4" r="3"/><path d="M1 14a6 6 0 0 1 12 0z"/></svg>
    <span>By Admin</span>
  </div>
  <a class="btn" href="#">READ ALL POSTS</a>
  <div class="dots"><span></span><span></span><span></span></div>
</section>

<section class="say">
  <h2 class="section-title">WHAT OUR PUBLISHERS SAYS..</h2>
  <div class="quotes">
    <figure class="quote">
      <p>Aliquam molestie, mi et imperdiet euismod, dui purus auctor tellus, et interdum lacus lectus et ante. Sed accumsan sollicitudin sapien, sit amet adipiscing turpis gravida ac.</p>
      <div class="avatar" role="img" aria-label="Publisher portrait"></div><div class="quote-mark">”</div>
      <h4>NAME HEADING</h4><small>Company</small>
    </figure>
    <figure class="quote">
      <p>Aliquam molestie, mi et imperdiet euismod, dui purus auctor tellus, et interdum lacus lectus et ante. Sed accumsan sollicitudin sapien, sit amet adipiscing turpis gravida ac.</p>
      <div class="avatar" role="img" aria-label="Publisher portrait"></div><div class="quote-mark">”</div>
      <h4>NAME HEADING</h4><small>Company</small>
    </figure>
    <figure class="quote">
      <p>Aliquam molestie, mi et imperdiet euismod, dui purus auctor tellus, et interdum lacus lectus et ante. Sed accumsan sollicitudin sapien, sit amet adipiscing turpis gravida ac.</p>
      <div class="avatar" role="img" aria-label="Publisher portrait"></div><div class="quote-mark">”</div>
      <h4>NAME HEADING</h4><small>Company</small>
    </figure>
  </div>
</section>

<section class="news">
  <h2 class="section-title">LATEST NEWS</h2>
  <div class="news-row">
    <article class="news-item">
      <div class="news-img" role="img" aria-label="Robotic hand touching an AI chip" style="background:linear-gradient(135deg,#7a9a70,#c9d3cf 60%,#8a9aa8)"></div>
      <h4>NAM FERMENTUM VESTIBULUM</h4>
      <p>Aliquam molestie, mi et imperdiet euismod, dui purus auctor tellus, et interdum lacus lectus et ante iaculis viverra..</p>
    </article>
    <article class="news-item">
      <div class="news-img" role="img" aria-label="Man in glasses beside a digital brain graphic" style="background:linear-gradient(135deg,#0e2a5a,#2f6fb0 60%,#0d1f44)"></div>
      <h4>NAM FERMENTUM VESTIBULUM</h4>
      <p>Aliquam molestie, mi et imperdiet euismod, dui purus auctor tellus, et interdum lacus lectus et ante iaculis viverra..</p>
    </article>
    <article class="news-item">
      <div class="news-img" role="img" aria-label="Android figure working at a holographic interface" style="background:linear-gradient(135deg,#b9c6cf,#6d8ea8 55%,#dfe6ea)"></div>
      <h4>NAM FERMENTUM VESTIBULUM</h4>
      <p>Aliquam molestie, mi et imperdiet euismod, dui purus auctor tellus, et interdum lacus lectus et ante iaculis viverra..</p>
    </article>
  </div>
</section>

<footer class="footer">
  <div class="footer-brand"><i></i>varitoken</div>
  <p class="copy">Copyright © 2017.Company Name.<br>All Right Reserved</p>
  <div class="social"><span>Pagely</span><span>Chirpa</span><span>Vidora</span><span>Linkly</span><span>Circlo</span></div>

  <h5 style="left:358px">NAVIGATION</h5>
  <div class="links" style="left:358px">
    <span>Home</span><span>Clients</span><span>Who We Are</span><span>Careers</span><span>What We Do</span><span>News</span><span>Blog</span><span>Contact Us</span>
  </div>

  <h5 style="left:642px">CONTACT INFO</h5>
  <div class="contact">
    4120 Harlow Lane,<br>Kestrel, KT7 2LW
    <div><svg width="12" height="12" viewBox="0 0 12 12" fill="#ddd"><path d="M2 1h3l1 3-2 1a7 7 0 0 0 3 3l1-2 3 1v3c-6 0-9-3-9-9z"/></svg>1-800-555-0142</div>
    <div><svg width="12" height="10" viewBox="0 0 12 10" fill="#ddd"><rect width="12" height="10"/><path d="M0 0l6 5 6-5" stroke="#1b1b1b" fill="none"/></svg>info@varitoken.co</div>
  </div>

  <h5 style="left:883px">EMAIL SIGN UP</h5>
  <div class="signup-input">Enter Email Address</div>
  <div class="signup-btn">SIGN UP</div>
</footer>

</body>
</html>
```